Silver Harbor Dental Clinic Flyer

I need to make a flyer Design for my clinic (Silver Harbor Dental Clinic) Based in Philippines, Makati .
We are Providing dental Service for high end market in the Philippines. Our speciality is Dental Aesthetic/Beautification. Our targets are actors/actresses, athletes, middle to high end
We are going to place this flyers in places like Ridgeway Fitness . and other lifestyle related places

Target Market(s)

Mid to high market

Industry/Entity Type

Dental Clinic

Font styles to use
Serif

Requirements
Must have
• The flyer should Contain Our address and the services that we offer
• #4821 Orchid Tower Makati Dalisay Cor. Verano St. Lumen Square .Makati
• Email: info@silverharbor.example.ph
• mobile +639051274806
• Landline:(02)5162947
• instagram:@shdc.ph
• facebook:SHDC.ph
• Our Services :
• General Dentistry ,Orthodontics ,Cosmetic Dentistry ,Pediatric Dentistry ,Teeth Whitening,Dental Implants ,Wisdom Tooth Extraction,Root Canal Therapy
• Silver Harbor Kids Treatment:
• Teeth Cleaning , Flouride Application ,Tooth Colored Filing ,Extraction ,Pit and Fissure Sealants, Space Management
Nice to have
• Nice to have a nice tagline

```html
<!DOCTYPE html>
<html lang="en">
<head>
<meta charset="utf-8">
<title>Silver Harbor Dental Clinic Flyer</title>
<link rel="stylesheet" href="https://fonts.googleapis.com/css2?family=Crimson+Pro:wght@400;600;700;800&display=swap">
<style>
  :root {
    --slate: #56625f;
    --slate-dark: #3d4644;
    --charcoal: #3b3b3b;
    --panel-light: #eeeff0;
    --ink: #1d1d1d;
    --white: #ffffff;
    --backdrop: #e9e9e9;
    --logo-tone: #7d8a87;
  }
  * { box-sizing: border-box; margin: 0; padding: 0; }
  html, body {
    width: 1200px; height: 1200px; overflow: hidden;
    background: var(--backdrop);
    font-family: "Crimson Pro", Georgia, serif;
  }
  .flyer {
    position: absolute; left: 203px; top: 40px;
    width: 793px; height: 1120px;
    background: var(--white);
    overflow: hidden;
    box-shadow: 0 6px 18px rgba(0,0,0,0.25);
  }
  .abs { position: absolute; }
  .hero-photo {
    left: 0; top: 0; width: 793px; height: 538px;
    background: linear-gradient(160deg, #dfe8e6 0%, #c7d4d2 35%, #9aa6a8 60%, #2f3d6a 80%, #c9cfd3 100%);
  }
  .tagline-box {
    left: 522px; top: 0; width: 271px; height: 136px;
    background: var(--slate);
    border-bottom-left-radius: 40px;
    border-left: 3px solid #222; border-bottom: 3px solid #222;
    color: var(--white); padding: 22px 0 0 30px;
  }
  .tagline-box .lead { font-weight: 800; font-size: 42px; line-height: 1; letter-spacing: 0.5px; }
  .tagline-box .rest { font-size: 29px; line-height: 1.15; letter-spacing: 0.5px; }
  .divider-band {
    left: 377px; top: 537px; width: 416px; height: 12px;
    border-top: 5px solid var(--slate); border-bottom: 3px solid var(--slate);
    background: var(--white);
  }
  .info-panel {
    left: 377px; top: 549px; width: 416px; height: 482px;
    background: linear-gradient(180deg, #f6f6f7, var(--panel-light));
  }
  .shapes { left: 0; top: 420px; width: 793px; height: 620px; }
  .brand { left: 46px; width: 331px; top: 572px; text-align: center; color: var(--logo-tone); }
  .brand .name { font-size: 36px; font-weight: 600; letter-spacing: 2px; line-height: 1; }
  .brand .kind { font-size: 14px; letter-spacing: 6px; margin-top: 10px; }
  .clinic-photo {
    left: 86px; top: 679px; width: 257px; height: 165px;
    border: 3px solid var(--white);
    background: linear-gradient(90deg, #6c6f72 0%, #cfd2d4 45%, #b19467 100%);
  }
  .appointment { left: 46px; width: 331px; top: 874px; text-align: center; color: var(--white); font-size: 24px; }
  .call-band {
    left: 33px; top: 915px; width: 359px; height: 43px;
    background: var(--slate); color: var(--white);
    font-weight: 700; font-size: 28px; text-align: center; line-height: 43px;
  }
  .hours { left: 46px; width: 331px; top: 973px; text-align: center; color: var(--white); font-size: 21px; }
  .section-label {
    background: var(--slate); color: var(--white);
    font-weight: 700; font-size: 27px; line-height: 35px; padding-left: 9px;
    box-shadow: 2px 2px 0 rgba(0,0,0,0.15);
  }
  .services-label { left: 417px; top: 569px; width: 193px; }
  .kids-label { left: 427px; top: 805px; width: 242px; padding-left: 16px; }
  .portrait { border: 2px solid #222; }
  .portrait-adult { left: 432px; top: 629px; width: 141px; height: 141px; background: linear-gradient(160deg, #8a5a3c, #d9b49a 50%, #3f5f8f); }
  .portrait-child { left: 592px; top: 864px; width: 139px; height: 141px; background: linear-gradient(160deg, #e9d8b0, #d8a57c 50%, #b67a4a); }
  .service-list { list-style: none; font-size: 15px; font-weight: 600; color: var(--ink); line-height: 20.6px; }
  .service-list li { position: relative; padding-left: 17px; white-space: nowrap; }
  .service-list li::before {
    content: ""; position: absolute; left: 0; top: 8px;
    width: 5px; height: 5px; border-radius: 50%; background: #8e9896;
  }
  .services-list { left: 585px; top: 619px; }
  .kids-list { left: 419px; top: 870px; }
  .footer {
    left: 0; top: 1031px; width: 793px; height: 89px;
    background: var(--slate); color: var(--white);
    font-size: 15px; font-weight: 600; line-height: 19px;
  }
  .footer .pin { position: absolute; left: 40px; top: 20px; }
  .footer .address { position: absolute; left: 58px; top: 17px; width: 340px; }
  .footer .contact { position: absolute; left: 445px; top: 8px; width: 330px; }
  .footer .contact-line { display: flex; align-items: center; gap: 8px; }
  .footer .label { font-weight: 400; opacity: 0.85; }
</style>
</head>
<body>
  <main class="flyer">
    <div class="abs hero-photo" role="img" aria-label="Photo of a smiling woman doing sit-ups on a bench in a bright gym"></div>

    <div class="abs tagline-box">
      <div class="lead">Leave your</div>
      <div class="rest">Silver smile to us</div>
    </div>

    <div class="abs divider-band"></div>
    <div class="abs info-panel"></div>

    <svg class="abs shapes" viewBox="0 0 793 620" aria-hidden="true">
      <path d="M0 200 L0 611 L48 611 L48 120 Q10 150 0 200 Z" fill="#ffffff"/>
      <path d="M44 130 Q6 150 0 180" fill="none" stroke="#2e2e2e" stroke-width="7"/>
      <path d="M48 150 Q18 175 8 215" fill="none" stroke="#56625f" stroke-width="3"/>
      <path d="M46 611 L46 80 Q211 -30 377 80 L377 611 Z" fill="#3b3b3b" stroke="#ffffff" stroke-width="4"/>
      <path d="M377 602 L700 602 Q775 600 793 575 L793 582 Q778 608 700 611 L377 611 Z" fill="#3d4644"/>
    </svg>

    <div class="abs brand">
      <div class="name">SILVER HARBOR</div>
      <div class="kind">DENTAL CLINIC</div>
    </div>

    <div class="abs clinic-photo" role="img" aria-label="Photo of the clinic reception with a ribbon-tied opening flower stand"></div>

    <div class="abs appointment">FOR AN APPOINTMENT</div>
    <div class="abs call-band">CALL-+63 905 127 4806</div>
    <div class="abs hours">(10:00AM - 6:00PM)</div>

    <div class="abs section-label services-label">OUR SERVICES</div>
    <div class="abs portrait portrait-adult" role="img" aria-label="Portrait photo of a smiling woman with wavy brown hair"></div>
    <ul class="abs service-list services-list">
      <li>General Dentistry</li>
      <li>Orthodontics</li>
      <li>Cosmetic Dentistry</li>
      <li>Pediatric Dentistry</li>
      <li>Teeth Whitening</li>
      <li>Dental Implants</li>
      <li>Wisdom Tooth Extraction</li>
      <li>Root Canal Therapy</li>
    </ul>

    <div class="abs section-label kids-label">KIDS TREATMENT</div>
    <ul class="abs service-list kids-list">
      <li>Teeth Cleaning</li>
      <li>Flouride Application</li>
      <li>Tooth Colored Filing</li>
      <li>Extraction</li>
      <li>Pit and Fissure Sealants</li>
      <li>Space Management</li>
    </ul>
    <div class="abs portrait portrait-child" role="img" aria-label="Portrait photo of a smiling young girl with long hair"></div>

    <footer class="abs footer">
      <svg class="pin" width="12" height="16" viewBox="0 0 12 16" aria-hidden="true">
        <path d="M6 0 C2.7 0 0 2.6 0 5.9 C0 10 6 16 6 16 C6 16 12 10 12 5.9 C12 2.6 9.3 0 6 0 Z" fill="#ffffff"/>
        <circle cx="6" cy="6" r="2.4" fill="#56625f"/>
      </svg>
      <div class="address">#4821 Orchid Tower Makati Dalisay Cor. Verano St.<br>Lumen Square .Makati</div>
      <div class="contact">
        <div class="contact-line">
          <svg width="16" height="11" viewBox="0 0 18 12" aria-hidden="true">
            <rect x="0.75" y="0.75" width="16.5" height="10.5" fill="none" stroke="#ffffff" stroke-width="1.5"/>
            <path d="M1 1 L9 7 L17 1" fill="none" stroke="#ffffff" stroke-width="1.5"/>
          </svg>
          <span>info@silverharbor.example.ph</span>
        </div>
        <div class="contact-line"><span class="label">Mobile</span> +639051274806 <span class="label">Landline</span> (02)5162947</div>
        <div class="contact-line"><span class="label">Instagram</span> @shdc.ph <span class="label">Facebook</span> SHDC.ph</div>
      </div>
    </footer>
  </main>
</body>
</html>
```